依頼詳細
朝陽経済報を読むターゲットに対して
我々の広告を打ちます。

伝えたいことは「普通じゃダメなんです」
HPをご確認のうえ、ジムの印象などもご確認ください。
https://kx7fit.example/
記載項目
キャッチ:普通のおじさんでは、出世できない
リード:とはいえ、残念ながら日本は精神的に老化しやすい環境が揃っているそう。かっこよさは若い人の特権のように考えられ、『かっこよく歳を重ねる』という意識が少ない傾向にある。ぜひ、当ジムで「おじさん化対策」を実践して欲しい

黒地に白文字でのデザインを想定しております。
裏面に当社の情報をいれるため
引き付けて裏面をめくりたくなるようなA面のデザインを依頼させていただきます。
サイズ
A4
ページ数
片面
希望イメージ
シンプル 複雑
単色 カラフル
暗い 明るい
日常 高級
遊び心 厳粛
未来的 伝統的
女性的 男性的
希望する色
無彩色系
納品ファイル
• 高解像度JPG (.jpg)
• イラストレーター形式 (.ai)
補足説明
下記ロゴデータを画面どこかへ配置をお願いします。
我々で考えたデザイン案は下記になります。
これとは違うデザインをご提案いただきたいです。

「普通のおじさんでは出世できない」

提案いただいた中で、このキャッチを
「絶望」「恐怖」などで提案いただきましたが
「警告」として色味や主張をいただいた点が決め手となりました。
単色の差し色をも、新聞折り込みのチラシとしての相性も良く
弊社満場一致で可決となりました。

合計で60超の提案をいただきました。
皆様クリエイティブ溢れるアイディアをありがとうございました。

・キャッチコピーの受け取り方が想定と違う
・「おじさん」の中でもとらえられるイメージが違う

我々からの定義の中でも、
ご依頼方法を再考しないといけないなと考える学びもありました。
この度は皆様ご協力いただきありがとうございました!!

```html
<!DOCTYPE html>
<html lang="ja">
<head>
<meta charset="UTF-8">
<title>普通のオジサンでは、出世できない</title>
<link href="https://fonts.googleapis.com/css2?family=Noto+Serif+JP:wght@500&family=Noto+Sans+JP:wght@400;500&display=swap" rel="stylesheet">
<style>
  :root {
    --ink: #ffffff;
    --ink-soft: #e9e9e9;
    --shadow: #060606;
    --mid: #3a3a3a;
    --light: #8a8a8a;
  }
  html, body {
    margin: 0;
    padding: 0;
    width: 846px;
    height: 1200px;
    overflow: hidden;
    background: var(--shadow);
  }
  .poster {
    position: relative;
    width: 846px;
    height: 1200px;
    overflow: hidden;
    background: var(--shadow);
  }
  .poster__photo {
    position: absolute;
    inset: 0;
    background:
      radial-gradient(ellipse 48% 34% at 52% 30%, var(--light) 0%, var(--mid) 55%, transparent 100%),
      radial-gradient(ellipse 60% 55% at 50% 55%, #2a2a2a 0%, #141414 60%, var(--shadow) 100%);
  }
  .poster__veil {
    position: absolute;
    inset: 0;
    background: linear-gradient(to bottom, rgba(0,0,0,0.15) 0%, rgba(0,0,0,0.05) 40%, rgba(0,0,0,0.55) 70%, rgba(0,0,0,0.8) 100%);
  }
  .headline {
    position: absolute;
    inset: 0;
    margin: 0;
    font-family: "Noto Serif JP", serif;
    font-weight: 500;
    color: var(--ink);
    letter-spacing: 0.02em;
  }
  .headline__line {
    position: absolute;
    white-space: nowrap;
    line-height: 1;
  }
  .headline__line--first { left: 6px; top: 188px; font-size: 117px; }
  .headline__line--second { left: 285px; top: 372px; font-size: 104px; }
  .headline__line--third { left: 168px; top: 508px; font-size: 110px; }
  .lead {
    position: absolute;
    left: 126px;
    top: 752px;
    width: 700px;
    margin: 0;
    font-family: "Noto Sans JP", sans-serif;
    font-weight: 400;
    font-size: 25px;
    line-height: 36px;
    color: var(--ink-soft);
    letter-spacing: 0.01em;
  }
  .brand {
    position: absolute;
    left: 0;
    right: 0;
    top: 990px;
    display: flex;
    justify-content: center;
    align-items: center;
    gap: 16px;
  }
  .brand__mark {
    width: 58px;
    height: 58px;
    border: 2px solid var(--ink);
    border-radius: 50%;
    box-sizing: border-box;
  }
  .brand__text {
    font-family: "Noto Sans JP", sans-serif;
    font-weight: 500;
    color: var(--ink);
  }
  .brand__name {
    display: block;
    font-size: 30px;
    line-height: 1.2;
    letter-spacing: 0.04em;
  }
  .brand__tagline {
    display: block;
    font-size: 14px;
    line-height: 1.4;
    letter-spacing: 0.04em;
  }
</style>
</head>
<body>
  <main class="poster">
    <div class="poster__photo" role="img" aria-label="モノクロ写真：鍛え上げられた男性の上半身、胸と腹筋のアップ"></div>
    <div class="poster__veil"></div>

    <h1 class="headline">
      <span class="headline__line headline__line--first">普通のオジサン</span>
      <span class="headline__line headline__line--second">では、</span>
      <span class="headline__line headline__line--third">出世できない</span>
    </h1>

    <p class="lead">とはいえ、残念ながら日本は精神的に老化しやすい環境が揃っているそう。かっこよさは若い人の特権のように考えられ、『かっこよく歳を重ねる』という意識が少ない傾向にある。ぜひ、当ジムで「おじさん化対策」を実践して欲しい。</p>

    <div class="brand">
      <span class="brand__mark"></span>
      <span class="brand__text">
        <span class="brand__name">7Fのトレーニングスタジオ</span>
        <span class="brand__tagline">The training studio on the 7th floor</span>
      </span>
    </div>
  </main>
</body>
</html>
```